Need Letterhead and Business Card

I have a logo but i need new letterhead and biz cards. We are a real estate investment firm so we need very professional but also do not want to be old fashioned. We have 3 locations; Singapore, New York and Ponte Vedra Florida. I can provide full addresses if needed. If you have adjustments to our logo you would recommend we are open to them.
I will be putting in a separate project but we also need a template for our own powerpoint slide presentations and website.

Real Estate

```html
<!DOCTYPE html>
<html lang="en">
<head>
<meta charset="utf-8">
<title>Halden Business Cards</title>
<link rel="stylesheet" href="https://fonts.googleapis.com/css2?family=Open+Sans:wght@400;600;700&display=swap">
<style>
  :root {
    --navy: #0f4c8a;
    --gold: #c9a227;
    --ink: #3a3a3a;
    --paper: #ffffff;
    --backdrop: #e9e7e3;
  }
  * { margin: 0; padding: 0; box-sizing: border-box; }
  html, body { width: 1200px; height: 900px; overflow: hidden; }
  body {
    background: var(--backdrop);
    font-family: "Open Sans", Arial, sans-serif;
    color: var(--ink);
    position: relative;
  }
  .card {
    position: absolute;
    left: 280px;
    width: 640px;
    height: 366px;
    background: var(--paper);
    box-shadow: 0 6px 18px rgba(0,0,0,0.15);
    overflow: hidden;
  }
  .card--back { top: 60px; }
  .card--front { top: 474px; }

  .brand { display: flex; align-items: center; gap: 14px; }
  .brand-mark { width: 30px; height: 30px; background: var(--navy); }
  .brand-name {
    font-weight: 700;
    font-size: 64px;
    line-height: 1;
    color: var(--navy);
    letter-spacing: 1px;
  }
  .brand-rule { height: 2px; background: var(--navy); margin-top: 10px; }
  .brand-tagline {
    margin-top: 6px;
    font-size: 13.5px;
    font-weight: 600;
    color: var(--gold);
    text-transform: uppercase;
    letter-spacing: 0.2px;
  }

  .card--back .brand-block { position: absolute; left: 150px; top: 92px; width: 340px; }
  .back-address {
    position: absolute;
    left: 150px;
    top: 218px;
    font-size: 15px;
    line-height: 1.55;
    color: var(--ink);
  }

  .card--front .brand-block { position: absolute; left: 44px; top: 110px; width: 320px; }
  .brand-block--small .brand-name { font-size: 56px; }

  .contact {
    position: absolute;
    right: 26px;
    top: 44px;
    text-align: right;
  }
  .contact-name { font-size: 22px; font-weight: 700; color: var(--navy); line-height: 1.1; }
  .contact-title { font-size: 13px; margin-top: 2px; }
  .contact-address { font-size: 13.5px; line-height: 1.4; margin-top: 16px; }
  .contact-list { list-style: none; margin-top: 12px; font-size: 15px; line-height: 1.45; }
  .contact-list li { display: flex; justify-content: flex-end; align-items: center; gap: 10px; }
  .contact-list svg { width: 12px; height: 12px; fill: var(--navy); flex: none; }

  .card-bands { position: absolute; left: 0; bottom: 0; width: 640px; height: 44px; }
  .band-navy { fill: var(--navy); }
  .band-gold { fill: var(--gold); }
</style>
</head>
<body>

  <section class="card card--back" aria-label="Business card back">
    <div class="brand-block">
      <div class="brand">
        <span class="brand-mark"></span>
        <span class="brand-name">Halden</span>
      </div>
      <div class="brand-rule"></div>
      <div class="brand-tagline">Real Estate Investment &amp; Management</div>
    </div>
    <div class="back-address">
      <p>418 Meridian Lane, Riverton, CA 95702</p>
      <p>418 Meridian Lane, Riverton, CA 95702</p>
    </div>
  </section>

  <section class="card card--front" aria-label="Business card front">
    <div class="brand-block brand-block--small">
      <div class="brand">
        <span class="brand-mark"></span>
        <span class="brand-name">Halden</span>
      </div>
      <div class="brand-rule"></div>
      <div class="brand-tagline">Real Estate Investment &amp; Management</div>
    </div>

    <div class="contact">
      <p class="contact-name">Daniel Whitcombe</p>
      <p class="contact-title">Managing Member</p>
      <p class="contact-address">418 Meridian Lane,<br>Riverton, CA 95702</p>
      <ul class="contact-list">
        <li>(555) 204-3180
          <svg viewBox="0 0 12 12" aria-hidden="true"><path d="M2.5 0.8l2 2-1 1.4c.7 1.5 1.8 2.6 3.3 3.3l1.4-1 2 2-1.2 1.9C5.2 10.2 1.8 6.8 0.6 2z"/></svg>
        </li>
        <li>(555) 204-3181
          <svg viewBox="0 0 12 12" aria-hidden="true"><path d="M3 0h5v3H3zM1 4h10v5H9v3H3V9H1zM4 8v3h4V8z"/></svg>
        </li>
        <li>(555) 317-4492
          <svg viewBox="0 0 12 12" aria-hidden="true"><path d="M3 0h6v12H3zM4 1.5v8h4v-8z"/></svg>
        </li>
        <li>daniel@haldenrealty.com
          <svg viewBox="0 0 12 12" aria-hidden="true"><path d="M0 2h12v8H0zM1 3l5 3.5L11 3z"/></svg>
        </li>
        <li>www.haldenrealty.com
          <svg viewBox="0 0 12 12" aria-hidden="true"><path d="M6 0a6 6 0 100 12A6 6 0 006 0zM1.2 5.3h2.2c.1-1.5.5-2.8 1.1-3.7A4.9 4.9 0 001.2 5.3zm3.3 0h3c-.1-1.6-.7-3.1-1.5-3.9-.8.8-1.4 2.3-1.5 3.9zm4.1 0h2.2a4.9 4.9 0 00-3.3-3.7c.6.9 1 2.2 1.1 3.7zM1.2 6.7a4.9 4.9 0 003.3 3.7c-.6-.9-1-2.2-1.1-3.7zm3.3 0c.1 1.6.7 3.1 1.5 3.9.8-.8 1.4-2.3 1.5-3.9zm4.1 0c-.1 1.5-.5 2.8-1.1 3.7a4.9 4.9 0 003.3-3.7z"/></svg>
        </li>
      </ul>
    </div>

    <svg class="card-bands" viewBox="0 0 640 44" aria-hidden="true">
      <polygon class="band-navy" points="0,14 368,14 382,28 0,28"/>
      <polygon class="band-gold" points="392,4 640,4 640,44 426,44"/>
    </svg>
  </section>

</body>
</html>
```